Marlow Hullcraft

Creating a brochure for company that manufactures boats. 8x11
Cover: Black w/boat pictures (just the boat, not the background)
1st inside page: Maybe a gray background of some sort (fade).
2nd inside page:same
Back Cover: Black background

Please feel free to ask questions. Photos on the design have the name of the pic.

Target Market(s)

- Companies that sell boats
- Individuals looking for a new boat

Industry/Entity Type

It Company

Requirements
Must have
• The brochure must have 4 pages and use all of the photos provided in the slots notes on the handwritten design idea.

```html
<!DOCTYPE html>
<html lang="en">
<head>
<meta charset="utf-8">
<title>Marlow Hullcraft Brochure Spread</title>
<link rel="stylesheet" href="https://fonts.googleapis.com/css2?family=Oswald:wght@500;600&family=Roboto+Condensed:wght@400;700&display=swap">
<style>
:root{
  --ink:#000;
  --gold:#f2b705;
  --spine-dark:#5a3d0c;
  --spine-light:#b8862a;
  --rule:#3a3a3a;
  --white:#fff;
}
*{margin:0;padding:0;box-sizing:border-box}
html,body{width:1200px;height:927px;overflow:hidden;background:var(--ink)}
.spread{position:relative;width:1200px;height:927px;background:var(--ink);font-family:"Roboto Condensed",sans-serif;color:var(--white)}
.spine{position:absolute;left:600px;top:0;width:36px;height:927px;background:linear-gradient(90deg,var(--spine-dark),var(--spine-light) 50%,var(--spine-dark))}
.brand-title{position:absolute;left:33px;top:33px;font-family:"Oswald",sans-serif;font-weight:600;font-size:32px;line-height:38px;color:var(--gold);letter-spacing:.3px}
.brand-sub{position:absolute;left:33px;top:71px;font-family:"Oswald",sans-serif;font-weight:500;font-size:23px;line-height:28px;color:var(--white)}
.feature{position:absolute;width:385px}
.feature h3{font-family:"Oswald",sans-serif;font-weight:600;font-size:15px;line-height:18px;color:var(--gold);margin-bottom:4px;letter-spacing:.2px}
.feature p{font-size:15px;line-height:15.5px}
.thumb{position:absolute;width:155px;height:98px}
.rule{position:absolute;left:30px;width:550px;height:1px;background:var(--rule)}
.spec{position:absolute;left:651px;width:490px;font-weight:700;font-size:13.5px;line-height:16px}
.model{position:absolute;right:0;width:49px;background:var(--gold);color:var(--ink);font-family:"Oswald",sans-serif;font-weight:600;font-size:22px;display:flex;align-items:center;justify-content:center}
.boat{position:absolute;left:648px;width:552px}
.boat-220{top:61px;height:290px;background:
  radial-gradient(ellipse 46% 22% at 56% 52%,#f4f0c8 0%,#e8e2a6 45%,rgba(232,226,166,0) 100%),
  radial-gradient(ellipse 30% 18% at 22% 72%,#dfe8ef 0%,rgba(223,232,239,0) 100%),
  linear-gradient(180deg,#1d3d58 0%,#22527a 45%,#2c6a96 100%)}
.boat-260{top:406px;height:227px;background:
  radial-gradient(ellipse 46% 20% at 58% 40%,#f2f6fa 0%,#cfe0ee 40%,rgba(207,224,238,0) 100%),
  radial-gradient(ellipse 50% 10% at 58% 55%,#3f8fc8 0%,rgba(63,143,200,0) 100%),
  linear-gradient(180deg,#4a2e26 0%,#3a4650 14%,#1e3a4e 30%,#2f6688 60%,#163044 100%)}
.boat-262{top:689px;height:238px;background:
  radial-gradient(ellipse 48% 18% at 55% 70%,#38c4d4 0%,#2fb2c6 45%,rgba(47,178,198,0) 100%),
  radial-gradient(ellipse 40% 12% at 55% 48%,#f3f5f5 0%,rgba(243,245,245,0) 100%),
  linear-gradient(180deg,#86b2de 0%,#b9d2ea 18%,#c9b89a 30%,#6f8d7a 38%,#2a6f86 60%,#1a4f62 100%)}
</style>
</head>
<body>
<div class="spread">
  <h1 class="brand-title">MARLOW HULLCRAFT</h1>
  <h2 class="brand-sub">The New Era of Marlow Hullcraft</h2>

  <div class="thumb" role="img" aria-label="Boat deck seating beside a dock" style="left:30px;top:136px;background:radial-gradient(ellipse 50% 45% at 60% 70%,#e6e4dc,rgba(230,228,220,0)),linear-gradient(135deg,#4f7488,#9fb6c2 50%,#6a8a9a)"></div>
  <div class="feature" style="left:209px;top:142px"><h3>LOREM IPSUM CONSECTETUR</h3><p>Lorem ipsum dolor sit amet, consectetur adipiscing elit, sed do eiusmod tempor incididunt ut labore et dolore magna aliqua. Ut enim ad minim veniam, quis nostrud exercitation ullamco laboris nisi ut aliquip ex ea commodo consequat.</p></div>
  <div class="rule" style="top:268px"></div>

  <div class="feature" style="left:33px;top:296px"><h3>LOREM IPSUM CONSECTETUR</h3><p>Lorem ipsum dolor sit amet, consectetur adipiscing elit, sed do eiusmod tempor incididunt ut labore et dolore magna aliqua. Ut enim ad minim veniam, quis nostrud exercitation ullamco laboris nisi ut aliquip ex ea commodo consequat.</p></div>
  <div class="thumb" role="img" aria-label="Workshop worker spraying a hull in red light" style="left:426px;top:294px;background:radial-gradient(circle at 35% 40%,#f6d6da,#d23a4c 55%,#7a0f1c)"></div>
  <div class="rule" style="top:420px"></div>

  <div class="thumb" role="img" aria-label="Close-up of a deck hatch detail" style="left:30px;top:444px;background:linear-gradient(180deg,#4a2a1a 0%,#1c1a18 35%,#2a2a2a 50%,#d8cfb8 75%,#e6ddc6 100%)"></div>
  <div class="feature" style="left:205px;top:448px"><h3>LOREM IPSUM CONSECTETUR</h3><p>Lorem ipsum dolor sit amet, consectetur adipiscing elit, sed do eiusmod tempor incididunt ut labore et dolore magna aliqua. Ut enim ad minim veniam, quis nostrud exercitation ullamco laboris nisi ut aliquip ex ea commodo consequat.</p></div>
  <div class="rule" style="top:576px"></div>

  <div class="feature" style="left:33px;top:604px"><h3>LOREM IPSUM CONSECTETUR</h3><p>Lorem ipsum dolor sit amet, consectetur adipiscing elit, sed do eiusmod tempor incididunt ut labore et dolore magna aliqua. Ut enim ad minim veniam, quis nostrud exercitation ullamco laboris nisi ut aliquip ex ea commodo consequat.</p></div>
  <div class="thumb" role="img" aria-label="Cushioned bow seating in tan" style="left:426px;top:603px;background:radial-gradient(ellipse 55% 45% at 50% 55%,#e0cfae,#b49b74 60%,#5c4a36)"></div>
  <div class="rule" style="top:732px"></div>

  <div class="thumb" role="img" aria-label="Open storage compartments on deck" style="left:30px;top:758px;background:radial-gradient(ellipse 35% 40% at 72% 45%,#5d7a3e,rgba(93,122,62,0)),linear-gradient(135deg,#1f2c40,#e8e8e8 55%,#bfc4c4)"></div>
  <div class="feature" style="left:202px;top:763px"><h3>LOREM IPSUM CONSECTETUR</h3><p>Lorem ipsum dolor sit amet, consectetur adipiscing elit, sed do eiusmod tempor incididunt ut labore et dolore magna aliqua. Ut enim ad minim veniam, quis nostrud exercitation ullamco laboris nisi ut aliquip ex ea commodo consequat.</p></div>

  <div class="spine"></div>

  <p class="spec" style="top:14px">LOA 22" / Beam 8'1" / Weight (without engine) 1950lb. (approx) / Fuel Tank 72gal<br>Draft 12" / Max. Horsepower 300HP / Deadrise 22"</p>
  <div class="model" style="top:0;height:58px">220</div>
  <div class="boat boat-220" role="img" aria-label="Pale yellow 22-foot bay boat running across dark blue open water"></div>

  <p class="spec" style="top:366px">LOA 26" / Beam 8'1" / Weight (without engine) 2350lb. (approx) / Fuel Tank 80gal<br>Draft 12"-14" / Max. Horsepower 350HP / Deadrise 22"</p>
  <div class="model" style="top:358px;height:48px">260</div>
  <div class="boat boat-260" role="img" aria-label="White 26-foot bay boat with blue hull moored at a wooden dock"></div>

  <p class="spec" style="top:650px">LOA 26" / Beam 8'6" / Weight (without engine) 4150lb. (approx) / Fuel Tank 150gal<br>Max. Horsepower 500HP / Deadrise 22"</p>
  <div class="model" style="top:642px;height:43px">262</div>
  <div class="boat boat-262" role="img" aria-label="Turquoise 26-foot center console boat with white T-top before a waterfront skyline"></div>
</div>
</body>
</html>
```